Brookline Wealth Guidance - Employer Benefit Brochure

We need to design a professional looking brochure that we can present to our existing client base, and assist in attracting new clients.
The current information is just provided in a word document, but we need to improve significantly.
The audience would be business leaders, HR decision makers and member policy committee members

Industry/Entity Type

Business

Font styles to use
Sans Serif

Colors
0255a3
f37122

```html
<!DOCTYPE html>
<html lang="en">
<head>
<meta charset="utf-8">
<title>Brookline Wealth Guidance – Employer Benefits Brochure</title>
<link href="https://fonts.googleapis.com/css2?family=Cormorant+Garamond:wght@600;700&family=Open+Sans:wght@300;400;600;700&display=swap" rel="stylesheet">
<style>
:root{
  --brand-blue:#0255a3;
  --brand-orange:#f37122;
  --sky-light:#cfe4fb;
  --sky-mid:#6fa8ec;
  --ink:#333;
  --ink-soft:#666;
  --rule:#bbb;
  --page-col:#d9d9d9;
  --backdrop:#e6e6e6;
}
*{box-sizing:border-box;margin:0;padding:0}
html,body{width:877px;height:1200px;overflow:hidden}
body{background:var(--backdrop);font-family:"Open Sans",Arial,sans-serif;color:var(--ink);position:relative}
.page{position:absolute;width:410px;height:565px;background:#fff;border:7px solid var(--brand-blue);overflow:hidden}
.page--cover{left:20px;top:20px}
.page--contents-a{left:447px;top:20px}
.page--contents-b{left:20px;top:610px}
.page--insurance{left:447px;top:610px}

/* cover */
.cover-mark{position:absolute;left:153px;top:30px;width:90px;height:90px;background:var(--brand-blue);border:5px solid var(--brand-orange)}
.cover-title{position:absolute;top:140px;width:100%;text-align:center;font-family:"Cormorant Garamond",Georgia,serif;font-weight:700;font-size:31px;line-height:38px;color:var(--brand-orange)}
.cover-sub{position:absolute;top:182px;width:100%;text-align:center;font-family:"Cormorant Garamond",Georgia,serif;font-weight:600;font-size:23px;line-height:27px;color:#444;z-index:1}
.cover-photo{position:absolute;left:0;right:0;top:282px;bottom:0;background:radial-gradient(ellipse at 55% 50%,#e4e4e4 0%,#f4e3d8 45%,#ffffff 85%)}

/* header band */
.band{position:absolute;left:6px;right:6px;top:8px;height:54px;background:linear-gradient(90deg,var(--sky-mid),var(--sky-light) 90%)}
.band-mark{position:absolute;left:6px;top:4px;width:46px;height:46px;background:var(--brand-blue);border:3px solid var(--brand-orange)}
.band-name{position:absolute;left:78px;top:12px;font-family:"Cormorant Garamond",Georgia,serif;font-weight:700;font-size:23px;color:#fff}

/* contents */
.toc{position:absolute;left:10px;right:10px;top:76px;height:446px;border:1px solid #ccc;border-radius:6px}
.toc-col{position:absolute;right:8px;top:0;bottom:0;width:24px;background:var(--page-col)}
.toc-label{position:absolute;left:8px;font-weight:300;font-size:13px;color:var(--ink-soft)}
.toc-list{position:absolute;left:200px;right:8px;list-style:none}
.toc-list li{display:flex;justify-content:space-between;height:17px;line-height:16px;font-size:9px;border-bottom:1px dotted var(--rule)}
.toc-list li .pg{width:24px;text-align:center}
.toc-list li.toc-head{color:var(--brand-orange);font-weight:700;border-bottom:none}
.toc-row{position:absolute;left:0;right:8px;display:flex;justify-content:space-between;align-items:center;font-weight:300;font-size:13px;color:var(--ink-soft);padding-left:8px;border-bottom:1px solid #ccc;height:20px}
.toc-row:last-of-type{border-bottom:none}
.toc-row .pg{width:24px;text-align:center;font-size:9px;color:var(--ink);font-weight:400}

/* footer */
.foot{position:absolute;left:6px;right:6px;bottom:8px;height:18px;padding:0 22px;background:var(--brand-orange);color:#fff;font-size:6px;display:flex;align-items:center;justify-content:center;gap:14px;white-space:nowrap}
.foot .folio{position:absolute;font-size:8px;font-weight:700}
.foot .folio--left{left:8px}
.foot .folio--right{right:8px}

/* insurance page */
.ins-title{position:absolute;top:26px;width:100%;text-align:center;font-family:"Cormorant Garamond",Georgia,serif;font-weight:700;font-size:22px;color:#222}
.ins-title .core{color:var(--brand-orange)}
.ins-intro{position:absolute;left:34px;right:34px;top:64px;font-size:8px;line-height:10px;color:#444}
.ins-points{position:absolute;left:22px;right:22px;top:126px;list-style:none}
.ins-points li{display:flex;align-items:center;gap:14px;height:58px;border-bottom:1px solid #ddd;font-size:11px;line-height:13px;color:#333}
.ins-icon{flex:none;width:54px;height:38px;border-radius:3px}
.ins-icon--family{background:linear-gradient(90deg,#8a1b1b,#d9d9d9)}
.ins-icon--debt{background:linear-gradient(135deg,#f1e6d8,#b38a5a)}
.ins-icon--budget{background:linear-gradient(135deg,#eeeeee,#8a8a8a)}
.ins-icon--health{background:linear-gradient(135deg,#ffffff,#3a8fd6)}
.ins-icon--partner{background:linear-gradient(135deg,#c9c9c9,#8b2a3a)}
.ins-outro{position:absolute;left:22px;right:22px;top:428px;font-size:8px;line-height:10px;color:#444}
</style>
</head>
<body>

<section class="page page--cover">
  <div class="cover-mark" aria-hidden="true"></div>
  <h1 class="cover-title">Brookline Wealth Guidance</h1>
  <p class="cover-sub">Employer Benefits<br>Partnership<br>Company Name</p>
  <div class="cover-photo" role="img" aria-label="Photo of four hands joining grey and red jigsaw puzzle pieces"></div>
</section>

<section class="page page--contents-a">
  <header class="band"><div class="band-mark" aria-hidden="true"></div><span class="band-name">Brookline Wealth Guidance</span></header>
  <div class="toc">
    <div class="toc-col"></div>
    <span class="toc-label" style="top:10px">Employer Benefits Program:</span>
    <ul class="toc-list" style="top:10px">
      <li class="toc-head"><span>Core Services</span></li>
      <li><span>Corporate Superannuation</span><span class="pg">1</span></li>
      <li><span>Insurance</span><span class="pg">2</span></li>
      <li><span>Financial Literacy &amp; Education</span><span class="pg">3</span></li>
      <li class="toc-head"><span>Additional Corporate Services</span></li>
      <li><span>Health Insurance</span><span class="pg">4</span></li>
      <li><span>Travel Insurance</span><span class="pg">4</span></li>
      <li><span>Key Person Insurance</span><span class="pg">5</span></li>
      <li><span>Asset &amp; Equipment Finance</span><span class="pg">5</span></li>
      <li><span>General &amp; Business Insurance</span><span class="pg">5</span></li>
      <li><span>Outplacement Solutions</span><span class="pg">6</span></li>
      <li><span>Professional Contractor Network</span><span class="pg">6</span></li>
    </ul>
    <span class="toc-label" style="top:234px">Employee Benefits Program:</span>
    <ul class="toc-list" style="top:234px">
      <li class="toc-head"><span>Core Services</span></li>
      <li><span>Superannuation Advice</span><span class="pg">8</span></li>
      <li><span>Insurance Advice</span><span class="pg">9</span></li>
      <li class="toc-head"><span>Additional Employee Services</span><span class="pg" style="color:var(--ink);font-weight:400">10</span></li>
      <li><span>Financial Planning</span><span class="pg"></span></li>
      <li><span>Wills &amp; Estate Planning</span><span class="pg">11</span></li>
      <li><span>Trauma (Critical Illness) Insurance</span><span class="pg">11</span></li>
      <li><span>Home &amp; Investment Lending</span><span class="pg">12</span></li>
      <li><span>Property Advice</span><span class="pg">13</span></li>
      <li><span>Car Leasing Finance</span><span class="pg">13</span></li>
    </ul>
    <div class="toc-row" style="top:400px"><span>Brookline Fee Flexibility</span><span class="pg">15</span></div>
    <div class="toc-row" style="top:422px"><span>Brookline Employee Benefits Team</span><span class="pg">17-19</span></div>
  </div>
  <footer class="foot"><span>14 HARBOUR LANE, EASTWOOD, 3021</span><span>PH: 03 5550 1842</span><span>WWW.BROOKLINEWG.COM</span><span>HELLO@BROOKLINEWG.COM</span></footer>
</section>

<section class="page page--contents-b">
  <header class="band"><div class="band-mark" aria-hidden="true"></div><span class="band-name">Brookline Wealth Guidance</span></header>
  <div class="toc">
    <div class="toc-col"></div>
    <span class="toc-label" style="top:10px">Employer Benefits Program:</span>
    <ul class="toc-list" style="top:10px">
      <li class="toc-head"><span>Core Services</span></li>
      <li><span>Corporate Superannuation</span><span class="pg">1</span></li>
      <li><span>Insurance</span><span class="pg">2</span></li>
      <li><span>Financial Literacy &amp; Education</span><span class="pg">3</span></li>
      <li class="toc-head"><span>Additional Corporate Services</span></li>
      <li><span>Health Insurance</span><span class="pg">4</span></li>
      <li><span>Travel Insurance</span><span class="pg">4</span></li>
      <li><span>Key Person Insurance</span><span class="pg">5</span></li>
      <li><span>Asset &amp; Equipment Finance</span><span class="pg">5</span></li>
      <li><span>General &amp; Business Insurance</span><span class="pg">5</span></li>
      <li><span>Outplacement Solutions</span><span class="pg">6</span></li>
      <li><span>Professional Contractor Network</span><span class="pg">6</span></li>
    </ul>
    <span class="toc-label" style="top:234px">Employee Benefits Program:</span>
    <ul class="toc-list" style="top:234px">
      <li class="toc-head"><span>Core Services</span></li>
      <li><span>Superannuation Advice</span><span class="pg">8</span></li>
      <li><span>Insurance Advice</span><span class="pg">9</span></li>
      <li class="toc-head"><span>Additional Employee Services</span><span class="pg" style="color:var(--ink);font-weight:400">10</span></li>
      <li><span>Financial Planning</span><span class="pg"></span></li>
      <li><span>Wills &amp; Estate Planning</span><span class="pg">11</span></li>
      <li><span>Trauma (Critical Illness) Insurance</span><span class="pg">11</span></li>
      <li><span>Home &amp; Investment Lending</span><span class="pg">12</span></li>
      <li><span>Property Advice</span><span class="pg">13</span></li>
      <li><span>Car Leasing Finance</span><span class="pg">13</span></li>
    </ul>
    <div class="toc-row" style="top:400px"><span>Brookline Fee Flexibility</span><span class="pg">15</span></div>
    <div class="toc-row" style="top:422px"><span>Brookline Employee Benefits Team</span><span class="pg">17-19</span></div>
  </div>
  <footer class="foot"><span class="folio folio--left">2</span><span>14 HARBOUR LANE, EASTWOOD, 3021</span><span>PH: 03 5550 1842</span><span>WWW.BROOKLINEWG.COM</span><span>HELLO@BROOKLINEWG.COM</span></footer>
</section>

<section class="page page--insurance">
  <h2 class="ins-title"><span class="core">CORE:</span> Insurance Advice Services</h2>
  <p class="ins-intro">As part of our initial engagement, we ensure that all members who have automatic insurance cover within the superannuation plan review their levels of cover. It's important that the cover is at an appropriate level for their individual needs. In working with your employees, we always consider these particular issues carefully before we make any recommendations or amendments to their insurance cover:</p>
  <ul class="ins-points">
    <li><div class="ins-icon ins-icon--family" role="img" aria-label="Photo of a row of family figures"></div><span>Their family - are they single, married, married with children or in subsequent marriages with children from both sides?</span></li>
    <li><div class="ins-icon ins-icon--debt" role="img" aria-label="Photo of scales balancing debt"></div><span>How much debt do they have? Mortgage, credit cards, personal loans…what assets do they own?</span></li>
    <li><div class="ins-icon ins-icon--budget" role="img" aria-label="Photo of a calculator and pen"></div><span>What is their monthly household budget?</span></li>
    <li><div class="ins-icon ins-icon--health" role="img" aria-label="Photo of a stethoscope"></div><span>What is the situation with their health? They may need to be underwritten</span></li>
    <li><div class="ins-icon ins-icon--partner" role="img" aria-label="Photo of a couple holding hands"></div><span>Review the insurance requirements for their partner, if appropriate</span></li>
  </ul>
  <p class="ins-outro">The right level of insurance cover is a very personal consideration - it depends on the employee's financial position and how they would like their family to be left financially and the cost of cover. Once the advice has been provided, agreed upon and actioned, we review and monitor the levels of cover each year to ensure that it remains relevant and is appropriate for their needs. We meet regularly with each member to discuss this as a part of their annual superannuation &amp; portfolio review.</p>
  <footer class="foot"><span>14 HARBOUR LANE, EASTWOOD, 3021</span><span>PH: 03 5550 1842</span><span>WWW.BROOKLINEWG.COM</span><span>HELLO@BROOKLINEWG.COM</span><span class="folio folio--right">9</span></footer>
</section>

</body>
</html>
```